New Architectural Firm Business Cards

New Business card to compliment previous pixel forum logo (attached). Please design a business card that is simple, modern, creative....please do not use "symbols", simply the logo and associated graphics/text. The front should contain name/address/phone/email/web address (with graphics).....back should be 100% graphic design using the logo somehow. Hoping for a two color (black and yellow) design. full bleed design, no borders

Target Market(s)

Commercial Architecture Clients

Industry/Entity Type

Architecture

Contact Information for Business Card

Please design a business card that is simple, modern, creative....please do not use "symbols", simply the logo and associated graphics/text. The front should contain name/address/phone/email/web address (with graphics).....back should be 100% graphic design using the logo somehow

Font styles to use
Sans Serif

Colors
FFF300
FFF600
FEFA6F
FFFEC7
FFFEE8

Requirements
Must have
• Clean, Modern Design
Should not have
• Stock images or "icons"

```html
<!DOCTYPE html>
<html lang="en">
<head>
<meta charset="utf-8">
<title>Norvale Architecture – Business Cards</title>
<link href="https://fonts.googleapis.com/css2?family=Arimo:wght@400;700&display=swap" rel="stylesheet">
<style>
  :root {
    --yellow: #f0c23b;
    --charcoal: #383334;
    --paper: #ececec;
    --ink: #2a2a2a;
    --muted: #6e6e6e;
    --contact-text: #e6e6e6;
    --backdrop: #c9ccd1;
  }
  * { box-sizing: border-box; margin: 0; padding: 0; }
  html, body {
    width: 1200px; height: 675px; overflow: hidden;
    background: var(--backdrop);
    font-family: "Arimo", Arial, sans-serif;
  }
  .stage {
    position: relative; width: 1200px; height: 675px;
    display: flex; align-items: center; justify-content: center; gap: 60px;
  }
  .card {
    position: relative; width: 520px; height: 297px; overflow: hidden;
    background: var(--yellow);
  }

  /* Back card */
  .card-back .dark-field {
    position: absolute; left: 0; top: 0; right: 0; height: 170px;
    background: var(--charcoal);
  }
  .card-back .brand {
    position: absolute; left: 0; right: 0; top: 52px;
    text-align: center; color: var(--yellow); font-weight: 700;
    line-height: 1;
  }
  .card-back .brand-name { display: block; font-size: 62px; letter-spacing: 2px; }
  .card-back .brand-sub { display: block; font-size: 24px; letter-spacing: 4px; margin-top: 8px; }

  /* Front card */
  .logo-panel {
    position: absolute; left: 0; top: 0; width: 215px; height: 132px;
    background: var(--charcoal); border-bottom-right-radius: 34px;
    display: flex; flex-direction: column; align-items: center; justify-content: center;
    color: var(--yellow); font-weight: 700; line-height: 1;
  }
  .logo-panel .brand-name { font-size: 28px; letter-spacing: 1px; }
  .logo-panel .brand-sub { font-size: 11px; letter-spacing: 2px; margin-top: 5px; }

  .contact-panel {
    position: absolute; left: 368px; top: 108px; right: 0; bottom: 0;
    background: var(--charcoal); border-top-left-radius: 38px;
    padding: 22px 8px 0 16px;
  }
  .contact-row {
    display: flex; align-items: center; gap: 10px;
    color: var(--contact-text); font-size: 9px; line-height: 1.25; margin-bottom: 16px;
    white-space: nowrap;
  }
  .contact-row svg { flex: none; }

  .profile-panel {
    position: absolute; left: 0; top: 142px; width: 356px; bottom: 0;
    background: var(--paper); border-top-right-radius: 16px;
  }
  .portrait-ring {
    position: absolute; left: 139px; top: 110px; width: 78px; height: 78px;
    border-radius: 50%; background: #f2f2f2; border: 5px solid var(--yellow);
  }
  .person {
    position: absolute; left: 0; width: 356px; top: 198px; text-align: center;
  }
  .person-name { font-size: 26px; font-weight: 700; color: var(--ink); }
  .person-role { font-size: 14px; color: var(--muted); margin-top: 2px; }

  .address {
    position: absolute; left: 318px; top: 22px;
    display: flex; align-items: flex-start; gap: 8px;
    font-size: 8.5px; color: var(--ink); line-height: 1.3;
  }
</style>
</head>
<body>
<main class="stage">

  <section class="card card-back" aria-label="Card back">
    <div class="dark-field"></div>
    <div class="brand">
      <span class="brand-name">NORVALE</span>
      <span class="brand-sub">ARCHITECTURE</span>
    </div>
  </section>

  <section class="card card-front" aria-label="Card front">
    <div class="logo-panel">
      <span class="brand-name">NORVALE</span>
      <span class="brand-sub">ARCHITECTURE</span>
    </div>

    <div class="address">
      <svg width="12" height="16" viewBox="0 0 12 16" aria-hidden="true">
        <path d="M6 0a6 6 0 0 1 6 6c0 4-6 10-6 10S0 10 0 6a6 6 0 0 1 6-6z" fill="var(--charcoal)"/>
        <circle cx="6" cy="6" r="2.2" fill="var(--yellow)"/>
      </svg>
      <span>1234 Lorem ipsum dolor sit amet,<br>consectetur adipiscing elit</span>
    </div>

    <div class="profile-panel"></div>
    <div class="portrait-ring"></div>
    <div class="person">
      <div class="person-name">Mara Ellison</div>
      <div class="person-role">Chief Executive Officer</div>
    </div>

    <div class="contact-panel">
      <div class="contact-row">
        <svg width="18" height="18" viewBox="0 0 18 18" aria-hidden="true">
          <circle cx="9" cy="9" r="9" fill="var(--yellow)"/>
          <path d="M6 4.5l1.8 2.3-1 1.1a6 6 0 0 0 3.3 3.3l1.1-1 2.3 1.8-1 1.5c-3.8 0-7.7-3.9-7.7-7.7z" fill="var(--charcoal)"/>
        </svg>
        <span>+123456789<br>+234567890</span>
      </div>
      <div class="contact-row">
        <svg width="18" height="13" viewBox="0 0 18 13" aria-hidden="true">
          <rect x="0" y="0" width="18" height="13" fill="var(--yellow)"/>
          <path d="M0 0l9 7 9-7" fill="none" stroke="var(--charcoal)" stroke-width="1.4"/>
        </svg>
        <span>email@email.com</span>
      </div>
      <div class="contact-row">
        <svg width="18" height="18" viewBox="0 0 18 18" aria-hidden="true">
          <circle cx="9" cy="9" r="9" fill="var(--yellow)"/>
          <circle cx="9" cy="9" r="5.5" fill="none" stroke="var(--charcoal)" stroke-width="1.2"/>
          <path d="M3.5 9h11M9 3.5c-2.5 3-2.5 8 0 11M9 3.5c2.5 3 2.5 8 0 11" fill="none" stroke="var(--charcoal)" stroke-width="1"/>
        </svg>
        <span>www.loremipsum.com</span>
      </div>
    </div>
  </section>

</main>
</body>
</html>
```